Barrowdale Power Loft Chronic Pain Flyer

Double sided DL flyer required to promote a strength training studio to sufferers of chronic pain. Flyer will be displayed in osteopathy, chiropractic and massage clinics. Flyer should be clean, professional and appeal to an older (40+) demographic.

Target Market(s)

Chronic pain sufferers. Age 40+

Industry/Entity Type

Health And Wellness

Colors

Designer to choose colors to be used in the design.

Requirements
Must have
• See attached files for text copy and logo. Image(s) of people strength training with a coach or personal trainer, as well as images depicting pain in common parts of the body (such as those pictured in the supplied mock up)
• website address: barrowdalepowerloft.com.au
• phone number : 0452 918 064
• Street address: 4/83 Kinross Hill Rd, Barrowdale
Nice to have
• Images such as in the attached files.

```html
<!DOCTYPE html>
<html lang="en">
<head>
<meta charset="utf-8">
<title>Barrowdale Power Loft – Chronic Pain DL Flyer</title>
<link rel="stylesheet" href="https://fonts.googleapis.com/css2?family=Poppins:wght@400;500;600;700;800;900&display=swap">
<style>
  :root {
    --page: #f2f2f2;
    --charcoal: #2b2b2b;
    --charcoal-deep: #1c1c1c;
    --red: #d42a2a;
    --red-bright: #ee4035;
    --red-dark: #a81d22;
    --white: #ffffff;
    --ink: #1e1e1e;
  }
  * { box-sizing: border-box; margin: 0; padding: 0; }
  html, body { width: 1200px; height: 1200px; overflow: hidden; }
  body {
    background: var(--page);
    font-family: "Poppins", sans-serif;
    position: relative;
  }
  .flyer {
    position: absolute;
    top: 212px;
    width: 370px;
    height: 780px;
    overflow: hidden;
  }
  .flyer--front { left: 212px; background: linear-gradient(180deg, #3a3a3a 0%, var(--charcoal) 55%, var(--charcoal-deep) 100%); }
  .flyer--back { left: 618px; background: linear-gradient(180deg, #ffffff 30%, #ececec 80%, #d8d8d8 100%); }

  /* front */
  .front-photo {
    position: absolute; left: 0; top: 0; width: 370px; height: 320px;
    background:
      radial-gradient(ellipse 70px 50px at 50% 78%, rgba(222,60,60,.85), rgba(222,60,60,0) 100%),
      radial-gradient(ellipse 200px 260px at 50% 40%, #c9c9c9, #8a8a8a 60%, #3a3a3a 100%);
  }
  .front-photo::after {
    content: ""; position: absolute; left: 0; bottom: 0; width: 100%; height: 90px;
    background: linear-gradient(180deg, rgba(42,42,42,0), #363636);
  }
  .brand-name {
    position: absolute; left: 0; width: 100%; top: 352px;
    text-align: center; color: var(--white);
    font-weight: 600; font-size: 25px; letter-spacing: 1px; line-height: 1.15;
    text-transform: uppercase;
  }
  .headline {
    font-weight: 900; color: var(--white); text-transform: uppercase;
    letter-spacing: -1.5px; line-height: .84; text-align: center;
  }
  .flyer--front .headline { position: absolute; left: 0; width: 100%; top: 452px; font-size: 42px; }
  .swoosh { position: absolute; left: 0; width: 100%; }
  .contact { position: absolute; left: 0; width: 100%; text-align: center; }
  .contact__phone {
    font-weight: 700; font-size: 27px; line-height: 1.1;
    display: flex; align-items: center; justify-content: center; gap: 4px;
  }
  .contact__address { font-size: 17px; line-height: 1.15; margin-top: 5px; display: flex; justify-content: center; gap: 6px; }
  .contact__address svg { margin-top: 3px; flex: none; }
  .flyer--front .contact { top: 638px; color: var(--white); }
  .web-bar {
    position: absolute; left: 0; bottom: 0; width: 100%; height: 34px;
    background: linear-gradient(90deg, var(--red-dark), var(--red));
    color: var(--white); font-size: 18px; text-align: center; line-height: 34px;
  }
  .web-bar b { font-weight: 700; }

  /* back */
  .back-top { position: absolute; left: 0; top: 0; width: 370px; height: 230px; }
  .flyer--back .headline { position: absolute; left: 0; width: 100%; top: 28px; font-size: 41px; }
  .tagline {
    position: absolute; left: 38px; width: 296px; top: 136px; height: 23px;
    border: 1.5px solid var(--red); color: var(--red-bright);
    font-size: 15px; font-weight: 500; text-align: center; line-height: 20px;
  }
  .photo-knee {
    position: absolute; right: 0; top: 212px; width: 160px; height: 215px;
    background:
      radial-gradient(ellipse 42px 70px at 48% 58%, rgba(230,80,80,.9), rgba(230,80,80,0)),
      linear-gradient(160deg, #8d8d8d, #e9e9e9 70%, rgba(255,255,255,0));
  }
  .photo-shoulder {
    position: absolute; left: 0; top: 405px; width: 145px; height: 210px;
    background:
      radial-gradient(ellipse 35px 30px at 45% 20%, rgba(230,80,80,.8), rgba(230,80,80,0)),
      linear-gradient(90deg, #a9a9a9, #e5e5e5 80%, rgba(255,255,255,0));
  }
  .copy { position: absolute; color: var(--ink); font-size: 14.4px; line-height: 1.22; }
  .copy--intro { left: 26px; top: 262px; width: 198px; }
  .copy--studio { left: 153px; top: 432px; width: 210px; }
  .copy--studio p + p { margin-top: 12px; }
  .cta {
    position: absolute; left: 153px; top: 560px; width: 200px;
    color: var(--red); font-weight: 700; font-size: 14.6px; line-height: 1.28; text-transform: uppercase;
  }
  .flyer--back .contact { top: 662px; color: var(--ink); }
</style>
</head>
<body>

<section class="flyer flyer--front" aria-label="Flyer front">
  <div class="front-photo" role="img" aria-label="Black and white photo of a man's bare back, hands on lower back with red pain highlight"></div>
  <div class="brand-name">Barrowdale<br>Power Loft</div>
  <h1 class="headline">Health<br>Through<br>Strength</h1>
  <svg class="swoosh" style="top:580px" width="370" height="60" viewBox="0 0 370 60" aria-hidden="true">
    <path d="M50 40 C150 0 290 5 370 35 L370 48 C290 20 160 20 50 40Z" fill="var(--red)"/>
  </svg>
  <div class="contact">
    <div class="contact__phone">
      <svg width="22" height="22" viewBox="0 0 24 24" aria-hidden="true"><path d="M6.6 10.8a15.1 15.1 0 0 0 6.6 6.6l2.2-2.2a1 1 0 0 1 1-.25 11.4 11.4 0 0 0 3.6.57 1 1 0 0 1 1 1V20a1 1 0 0 1-1 1A17 17 0 0 1 3 4a1 1 0 0 1 1-1h3.5a1 1 0 0 1 1 1c0 1.25.2 2.45.57 3.570a1 1 0 0 1-.25 1z" fill="var(--red-bright)"/></svg>
      0452 918 064
    </div>
    <div class="contact__address">
      <svg width="14" height="18" viewBox="0 0 14 18" aria-hidden="true"><path d="M7 1a6 6 0 0 0-6 6c0 4.5 6 10 6 10s6-5.5 6-10a6 6 0 0 0-6-6z" fill="none" stroke="var(--red-bright)" stroke-width="2"/><circle cx="7" cy="7" r="2" fill="var(--red-bright)"/></svg>
      <span>4/83 Kinross Hill Rd,<br>Barrowdale, VIC, 3188</span>
    </div>
  </div>
  <div class="web-bar"><b>barrowdalepowerloft</b>.com.au</div>
</section>

<section class="flyer flyer--back" aria-label="Flyer back">
  <div class="photo-knee" role="img" aria-label="Black and white photo of hands holding a knee with red pain highlight"></div>
  <div class="photo-shoulder" role="img" aria-label="Black and white photo of a hand holding a shoulder with red pain highlight"></div>
  <svg class="back-top" viewBox="0 0 370 230" aria-hidden="true">
    <path d="M0 0 H370 V165 C300 200 200 230 110 215 C60 207 25 195 0 160Z" fill="var(--charcoal)"/>
    <path d="M0 160 C40 205 110 225 180 220 C260 214 320 190 370 165 V180 C320 205 260 228 175 226 C100 224 35 205 0 160Z" fill="var(--red)"/>
  </svg>
  <h2 class="headline">Health<br>Through<br>Strength</h2>
  <div class="tagline">YOU DON'T HAVE TO LIVE IN PAIN</div>

  <p class="copy copy--intro">Strength training has been shown to improve many chronic pain conditions and is now routinely recommended by medical and health professionals.</p>
  <div class="copy copy--studio">
    <p>Our private studio provides high quality strength training by expert strength coaches.</p>
    <p>We've helped countless people improve or eliminate chronic pain,</p>
  </div>
  <p class="cta">Contact us today<br>and find out how<br>we can help you.</p>

  <svg class="swoosh" style="top:608px" width="370" height="60" viewBox="0 0 370 60" aria-hidden="true">
    <path d="M55 30 C150 0 290 5 370 28 L370 50 C290 18 160 18 55 30Z" fill="var(--red)"/>
  </svg>
  <div class="contact">
    <div class="contact__phone">
      <svg width="22" height="22" viewBox="0 0 24 24" aria-hidden="true"><path d="M6.6 10.8a15.1 15.1 0 0 0 6.6 6.6l2.2-2.2a1 1 0 0 1 1-.25 11.4 11.4 0 0 0 3.6.57 1 1 0 0 1 1 1V20a1 1 0 0 1-1 1A17 17 0 0 1 3 4a1 1 0 0 1 1-1h3.5a1 1 0 0 1 1 1c0 1.25.2 2.45.57 3.57a1 1 0 0 1-.25 1z" fill="var(--red)"/></svg>
      0452 918 064
    </div>
    <div class="contact__address">
      <svg width="14" height="18" viewBox="0 0 14 18" aria-hidden="true"><path d="M7 1a6 6 0 0 0-6 6c0 4.5 6 10 6 10s6-5.5 6-10a6 6 0 0 0-6-6z" fill="none" stroke="var(--red)" stroke-width="2"/><circle cx="7" cy="7" r="2" fill="var(--red)"/></svg>
      <span>4/83 Kinross Hill Rd,<br>Barrowdale, VIC, 3188</span>
    </div>
  </div>
  <div class="web-bar"><b>barrowdalepowerloft</b>.com.au</div>
</section>

</body>
</html>
```